New Pump Website Design Needed

We need a homepage concept for a pump website rebuild.

The navigation at the top must be:
Home - About Us - Pump Stations - Pumps - Electrical - Drainage - Environmental - Accessories - Contact Us

The homepage should have the the following structure:
Logo
Navigation
Rotating Banner
Content + Picture of PDF Flipbook to download/ view
Featured Products (in one row - approx 4)
Footer

The footer must include:
Left side - navigation small.
"Copyright QuickRun 2014. All Rights reserved"

Right side: "Website by Sites Built Simple"

Content and imagery, and Logo can be taken from their existing website: harbourvalvetech.co.nz

We have attached a copy of their New PDF - the new website design must reflect this (Use block colours/ different colours for the navigation items/ incorporate the footer image).

Font styles to use
Sans Serif

Requirements
Must have
• Features from their brochure brought in (colour scheme and footer feature)
Should not have
• Any Social Media Icons

```html
<!DOCTYPE html>
<html lang="en">
<head>
<meta charset="utf-8">
<title>QuickRun – Providing Pumping Solutions</title>
<link rel="stylesheet" href="https://fonts.googleapis.com/css2?family=Exo+2:wght@300;400;500&family=Raleway:wght@600;700&family=Roboto:ital,wght@0,400;0,500;0,700;1,700&display=swap">
<style>
:root{
  --blue:#1f64ad;
  --blue-dark:#0e4a8c;
  --blue-light:#3c8fd6;
  --page:#f7f7f7;
  --text:#333;
  --heading:#555;
  --green:#6cb52b;
  --orange:#e99a22;
  --purple:#6b3570;
  --red:#d8222c;
  --orange-red:#ea5a1a;
  --forest:#0d5a22;
  --teal:#1c9aa3;
  --maroon:#7e1015;
  --footer-gray:#a9a9a9;
  --footer-red:#e0262c;
  --footer-blue:#0f4b93;
}
*{margin:0;padding:0;box-sizing:border-box}
html,body{width:915px;height:1200px;overflow:hidden}
body{position:relative;background:var(--page);font-family:"Roboto",Arial,sans-serif;color:var(--text)}
.abs{position:absolute}
.header-bg{left:0;top:0}
.brand{left:74px;top:36px;color:#fff}
.brand-name{font-family:"Roboto",sans-serif;font-weight:700;font-size:34px;letter-spacing:1px;line-height:1}
.brand-name::after{content:"";display:inline-block;width:22px;height:22px;background:#fff;border-radius:50%;margin-left:10px;vertical-align:2px}
.brand-tag{font-size:10px;margin:14px 0 0 132px;white-space:nowrap}
.contact{left:712px;top:56px;color:#fff}
.contact svg{position:absolute;left:0;top:2px}
.contact-phone{margin-left:31px;font-weight:700;font-size:14px}
.contact-mail{margin-left:35px;font-size:8px;color:#9fe06a;margin-top:1px}
.nav{left:75px;top:128px;display:flex;height:30px}
.nav a{display:flex;align-items:center;justify-content:center;color:#fff;text-decoration:none;font-size:11px;text-transform:uppercase;border-radius:4px 4px 0 0;margin-right:1px;letter-spacing:.2px}
.banner-frame{left:75px;top:158px;width:763px;height:346px;background:#fff;box-shadow:0 10px 12px -8px rgba(0,0,0,.25)}
.banner-photo{left:5px;top:6px;width:754px;height:334px;background:linear-gradient(180deg,#9fb8e6 0%,#c0d1ee 40%,#6a7445 50%,#6b5a44 75%,#5b4a38 100%)}
.banner-title{left:270px;top:332px;color:#fff;font-family:"Exo 2",sans-serif;text-shadow:0 1px 3px rgba(0,0,0,.4);line-height:1.05}
.banner-title .strong{font-size:41px;font-weight:400}
.banner-title .light{font-size:30px;font-weight:300}
.banner-title .line2{font-size:31px;font-weight:300;letter-spacing:1px}
.btn-guide{left:313px;top:437px;width:270px;height:35px;border-radius:10px;background:linear-gradient(#7fcc3a,#4d9c1c);color:#1d2a10;font-weight:700;font-size:16px;display:flex;align-items:center;justify-content:center;box-shadow:0 2px 3px rgba(0,0,0,.3);letter-spacing:.3px}
.welcome{left:83px;top:556px;width:743px;text-align:center}
.welcome h1{font-family:"Raleway",sans-serif;font-weight:700;font-size:14px;color:var(--heading);letter-spacing:.3px}
.welcome p{font-size:10.2px;line-height:16.8px;margin-top:6px;color:#333}
.btn-more{left:414px;top:657px;width:90px;height:30px;background:var(--orange);border-radius:3px;color:#fff;font-size:12px;display:flex;align-items:center;justify-content:center;box-shadow:0 2px 0 #b9b9b9}
.card{top:752px;width:232px;height:129px;overflow:hidden}
.card-photo{left:0;top:0;width:232px;height:129px;background:linear-gradient(160deg,#cfcac0 0%,#8d8e8a 40%,#3b6fb4 62%,#6e6a60 100%)}
.card-label{left:0;bottom:0;width:232px;height:28px;color:#fff;font-family:"Exo 2",sans-serif;font-size:18px;padding-left:13px;line-height:28px}
.card svg{position:absolute;right:0;bottom:0}
.news{top:946px;left:0;width:915px;height:185px;background:var(--footer-gray);color:#fff}
.news h2{font-size:16px;font-weight:700;letter-spacing:.8px}
.connect{left:98px;top:29px}
.connect p{font-size:9.5px;line-height:14px;margin-top:12px;width:170px}
.newsletter{left:345px;top:26px}
.newsletter h2{margin-left:36px;margin-top:3px}
.newsletter svg{position:absolute;left:0;top:0}
.newsletter .lead{font-style:italic;font-weight:700;font-size:9px;margin:13px 0 0 5px;width:220px;line-height:11px;word-spacing:1.5px}
.news-input{left:0;top:67px;width:225px;height:26px;border-radius:13px;background:linear-gradient(#fafafa,#dcdcdc);border:1px solid #c6c6c6;color:#444;font-size:9px;padding-left:12px;line-height:24px}
.news-btn{left:164px;top:103px;width:61px;height:21px;border-radius:10px;background:#2b2b2b;color:#fff;font-size:9.5px;display:flex;align-items:center;justify-content:center}
.foot-brand{left:654px;top:38px;color:#fff}
.foot-brand .brand-name{font-size:25px}
.foot-brand .brand-name::after{width:16px;height:16px;margin-left:8px}
.foot-brand .brand-tag{font-size:8px;margin:8px 0 0 96px}
.rule{left:0;top:1131px;width:915px;height:5px;background:var(--footer-red)}
.bottom{left:0;top:1136px;width:915px;height:64px;background:var(--footer-blue);color:#fff}
.foot-nav{left:76px;top:13px;font-size:10px;font-weight:500;white-space:nowrap}
.foot-nav span{margin:0 6px}
.copyright{left:76px;top:31px;font-size:9px}
.credit{right:77px;top:15px;font-size:9px}
</style>
</head>
<body>

<svg class="abs header-bg" width="915" height="330" viewBox="0 0 915 330" aria-hidden="true">
  <defs>
    <linearGradient id="hdr" x1="0" y1="0" x2="0" y2="1">
      <stop offset="0" stop-color="#2a6fb6"/>
      <stop offset="1" stop-color="#1a5ea6"/>
    </linearGradient>
  </defs>
  <path d="M0 318 Q457 120 915 318 L915 0 L0 0 Z" fill="var(--blue-light)"/>
  <path d="M0 306 Q457 108 915 306 L915 0 L0 0 Z" fill="url(#hdr)"/>
</svg>

<div class="abs brand">
  <div class="brand-name">QuickRun</div>
  <div class="brand-tag">Providing Pumping Solutions</div>
</div>

<div class="abs contact">
  <svg width="24" height="20" viewBox="0 0 24 20" aria-hidden="true">
    <path d="M2 7 Q12 -1 22 7 L19 9 L16 6 Q12 4 8 6 L5 9 Z" fill="#fff"/>
    <path d="M6 10 H18 L20 19 H4 Z" fill="#fff"/>
    <circle cx="12" cy="14" r="3" fill="var(--blue)"/>
  </svg>
  <div class="contact-phone">(555)-010-248</div>
  <div class="contact-mail">E-mail: hello@quickrun.example</div>
</div>

<nav class="abs nav">
  <a style="width:71px;background:var(--green)">Home</a>
  <a style="width:76px;background:var(--orange)">About Us</a>
  <a style="width:107px;background:var(--purple)">Pumpstations</a>
  <a style="width:70px;background:var(--red)">Pumps</a>
  <a style="width:97px;background:var(--orange-red)">Electrical</a>
  <a style="width:98px;background:var(--forest)">Drainage</a>
  <a style="width:119px;background:var(--teal)">Environmental</a>
  <a style="width:120px;background:var(--maroon)">Accessories</a>
</nav>

<div class="abs banner-frame">
  <div class="abs banner-photo" role="img" aria-label="Workers with a backhoe digging a trench to lay pipe in a ploughed field"></div>
</div>
<div class="abs banner-title">
  <div><span class="strong">Lorem Ipsum</span> <span class="light">has</span></div>
  <div class="line2">been the industry's</div>
</div>
<div class="abs btn-guide">Download Product Guide</div>

<section class="abs welcome">
  <h1>WELCOME TO HARBOURLINE PUMPS.</h1>
  <p>Lorem Ipsum has been the industry's standard dummy text ever since the 1500s, when an unknown printer took a galley of type and scrambled it to make a type specimen book. It has survived not only five centuries, but also the leap into electronic typesetting, remaining essentially unchanged. It was popularised in the 1960s with the release of Transferset sheets containing Lorem Ipsum passages, and more recently with desktop publishing software like LayoutWorks including versions of Lorem Ipsum.</p>
</section>
<div class="abs btn-more">Read More</div>

<div class="abs card" style="left:76px">
  <div class="abs card-photo" role="img" aria-label="Workers fitting a blue valve in a concrete pump chamber"></div>
  <div class="abs card-label" style="background:var(--maroon)">Lorem Ipsum</div>
  <svg width="100" height="80" viewBox="0 0 100 80" aria-hidden="true"><path d="M100 0 V80 H0 Z" fill="#000"/><g transform="rotate(-40 60 52)" fill="#fff"><text x="46" y="57" font-family="Exo 2,sans-serif" font-size="14">INFO</text><path d="M30 50 l6 8 l6 -8 M36 44 v13" stroke="#fff" stroke-width="2" fill="none"/></g></svg>
</div>
<div class="abs card" style="left:342px">
  <div class="abs card-photo" style="background:linear-gradient(160deg,#5f5e56 0%,#b9ae98 35%,#5b7796 60%,#a89e8c 100%)" role="img" aria-label="Worker assembling a long blue pump shaft on sandy ground"></div>
  <div class="abs card-label" style="background:var(--teal)">Lorem Ipsum</div>
  <svg width="100" height="80" viewBox="0 0 100 80" aria-hidden="true"><path d="M100 0 V80 H0 Z" fill="#000"/><g transform="rotate(-40 60 52)" fill="#fff"><text x="46" y="57" font-family="Exo 2,sans-serif" font-size="14">INFO</text><path d="M30 50 l6 8 l6 -8 M36 44 v13" stroke="#fff" stroke-width="2" fill="none"/></g></svg>
</div>
<div class="abs card" style="left:606px">
  <div class="abs card-photo" role="img" aria-label="Workers fitting a blue valve in a concrete pump chamber"></div>
  <div class="abs card-label" style="background:var(--forest)">Lorem Ipsum</div>
  <svg width="100" height="80" viewBox="0 0 100 80" aria-hidden="true"><path d="M100 0 V80 H0 Z" fill="#000"/><g transform="rotate(-40 60 52)" fill="#fff"><text x="46" y="57" font-family="Exo 2,sans-serif" font-size="14">INFO</text><path d="M30 50 l6 8 l6 -8 M36 44 v13" stroke="#fff" stroke-width="2" fill="none"/></g></svg>
</div>

<section class="abs news">
  <div class="abs connect">
    <h2>Connect With Us</h2>
    <p>Click on the social media icons below and stay connected with us across the web and throughout your day.</p>
  </div>
  <div class="abs newsletter">
    <svg width="30" height="28" viewBox="0 0 30 28" aria-hidden="true">
      <rect x="1" y="4" width="24" height="20" rx="2" fill="#e8f2fb"/>
      <rect x="1" y="4" width="24" height="6" fill="#3a8fd6"/>
      <path d="M8 26 L26 6 L29 9 L11 28 Z" fill="#333"/>
    </svg>
    <h2>Subscribe to newsletter</h2>
    <div class="lead">Lorem Ipsum is simply dummy text of the printing and typesetting</div>
    <div class="abs news-input">Enter Newsletter</div>
    <div class="abs news-btn">Subscribe</div>
  </div>
  <div class="abs foot-brand">
    <div class="brand-name">QuickRun</div>
    <div class="brand-tag">Providing Pumping Solutions</div>
  </div>
</section>

<div class="abs rule"></div>
<footer class="abs bottom">
  <div class="abs foot-nav">Home<span>|</span>About Us<span>|</span>Pump Stations<span>|</span>Pumps<span>|</span>Electrical<span>|</span>Drainage<span>|</span>Environmental<span>|</span>Accessories</div>
  <div class="abs copyright">Copyright QuickRun 2014. All Rights reserved</div>
  <div class="abs credit">Website by Sites Built Simple</div>
</footer>

</body>
</html>
```